Business Card Design Project

I need a business card design for our new logo, please check the logo at the following link:
https://www.filecrate.net/s/q7rtx2pw9kd41m/FernLoop.png
The address on the business card:
Av. Gervásio Tavares 418 sala 207
Barra da Tijuca, Rio de Janeiro, RJ
CEP: 22714-380
Brasil
Phone: +55 21 86347215
e-mail: osvaldo@fernloop.com.br
Updates
Thank you all for sending your designs, we will not provide feedback because there are too many designs, on December 3 we will pick the best design according to our point of view. Please keep posting.
Osvaldo
Industry/Entity Type
Business
Look and feel
Each slider illustrates characteristics of the customer's brand and the style your logo design should communicate.

```html
<!DOCTYPE html>
<html lang="pt-BR">
<head>
<meta charset="utf-8">
<title>FernLoop — Business Card</title>
<link rel="stylesheet" href="https://fonts.googleapis.com/css2?family=Source+Sans+3:wght@400;700;800&display=swap">
<style>
  :root {
    --page-bg: #d9d9d9;
    --card-yellow: #f2c10f;
    --card-yellow-deep: #e0a900;
    --card-yellow-light: #f7cf2a;
    --olive-dark: #6b5a1e;
    --ink: #1c1a14;
    --logo-light: #ffffff;
    --edge-shadow: rgba(0,0,0,0.28);
  }
  * { box-sizing: border-box; margin: 0; padding: 0; }
  html, body {
    width: 1200px; height: 1200px; overflow: hidden;
    background: var(--page-bg);
    font-family: "Source Sans 3", "Myriad Pro", Arial, sans-serif;
  }
  .sheet {
    width: 1200px; height: 1200px;
    display: flex; flex-direction: column; align-items: center; justify-content: center;
    gap: 60px;
  }
  .card {
    position: relative;
    width: 900px; height: 514px;
    overflow: hidden;
    box-shadow: 0 10px 26px var(--edge-shadow);
  }

  /* Front side */
  .front-backdrop {
    position: absolute; inset: 0;
    background: radial-gradient(ellipse 70% 75% at 50% 50%,
      var(--olive-dark) 0%, var(--card-yellow-deep) 55%, var(--card-yellow) 100%);
  }
  .front-wordmark {
    position: absolute; inset: 0;
    display: flex; align-items: center; justify-content: center; gap: 22px;
  }
  .front-wordmark__dot {
    width: 54px; height: 54px; border-radius: 50%;
    background: var(--logo-light);
  }
  .front-wordmark__name {
    font-size: 120px; font-weight: 800; line-height: 1;
    color: var(--logo-light); letter-spacing: -1px;
  }

  /* Back side */
  .card--back {
    background: linear-gradient(180deg, var(--card-yellow-light), var(--card-yellow));
  }
  .back-circle {
    position: absolute; left: 0; top: 0;
    width: 900px; height: 514px;
  }
  .contact {
    position: absolute; top: 52px; right: 350px;
    text-align: right; color: var(--ink);
  }
  .contact__name { font-size: 27px; font-weight: 400; line-height: 1.15; margin-right: -60px; }
  .contact__role { font-size: 15px; margin-top: 6px; margin-right: -60px; }
  .contact__address {
    margin-top: 30px; font-style: normal;
    font-size: 19px; line-height: 1.42;
  }
  .back-wordmark {
    position: absolute; left: 505px; top: 305px;
    display: flex; align-items: center; gap: 14px;
  }
  .back-wordmark__dot {
    width: 34px; height: 34px; border-radius: 50%;
    background: var(--ink);
  }
  .back-wordmark__name {
    font-size: 76px; font-weight: 800; line-height: 1;
    color: var(--ink); letter-spacing: -1px;
  }
</style>
</head>
<body>
<main class="sheet">
  <section class="card card--front" aria-label="Card front">
    <div class="front-backdrop" role="img" aria-label="Decorative diagonal yellow and dark stripe pattern"></div>
    <div class="front-wordmark">
      <span class="front-wordmark__dot"></span>
      <span class="front-wordmark__name">FernLoop</span>
    </div>
  </section>

  <section class="card card--back" aria-label="Card back">
    <svg class="back-circle" viewBox="0 0 900 514" aria-hidden="true">
      <defs>
        <radialGradient id="circleFill" cx="0.35" cy="0.3" r="0.8">
          <stop offset="0" stop-color="#f8d02c"/>
          <stop offset="1" stop-color="#e8b300"/>
        </radialGradient>
        <filter id="circleShadow" x="-20%" y="-20%" width="140%" height="140%">
          <feDropShadow dx="-6" dy="4" stdDeviation="8" flood-color="#8a6a00" flood-opacity="0.45"/>
        </filter>
      </defs>
      <circle cx="770" cy="330" r="290" fill="url(#circleFill)" filter="url(#circleShadow)"/>
    </svg>

    <div class="contact">
      <p class="contact__name">Firstname Lastname</p>
      <p class="contact__role">Function</p>
      <address class="contact__address">
        Av. Gervásio Tavares 418 sala 207<br>
        Barra da Tijuca, Rio de Janeiro, RJ<br>
        CEP: 22714-380<br>
        Brasil<br>
        +55 21 86347215<br>
        osvaldo@fernloop.com.br
      </address>
    </div>

    <div class="back-wordmark">
      <span class="back-wordmark__dot"></span>
      <span class="back-wordmark__name">FernLoop</span>
    </div>
  </section>
</main>
</body>
</html>
```